Uncoded front page web design for wedding and event planning company

Hi.

I am launching a wedding and event planning company called Silver Fern Gatherings and need a professional and appealing web design.

So, let me explain my company. I am based in Swindon in Wiltshire but the company will plan weddings and events in Oxfordshire, Wiltshire, Berkshire and London.

We will plan weddings, birthdays, conferences, product launches, fashion shows and conventions but the main focus of the website at this stage should be the weddings with all the other occasions being covered under a single 'events' heading.

My contact details for the website should be:
Maureen Pollard
maureen@silverferngatherings.co.uk
01632 960571 / 07700 900384

I'd like the website to feel clean, bright and elegant and be set against a white or off-white background. My logo is purple and I'd therefore like some purple incorporated into the design although feel free to use a more muted purple as my one might be a little bright? I'm also considering whether it would look nice paired with a little of the colour gold - maybe as a font colour in places?? I'll leave you to figure that one out as your design eye will be better than mine but for your reference below is my purple colour and my suggested gold one....

My purple colour is Pantone 2592 C but feel free to use others
My suggested gold I'm looking at is Pantone 14-1041 TCX

I would like to incorporate a Facebook feed in the front page if possible, if it looks right. I'd also like to include a variety of pictures as well so I've included a few in a Dropbox folder which is linked below. Please don't feel obliged to use them all by any means (there's loads!) but you've got a few there to play with. If you find any other royalty free images you'd rather use please go ahead but on the understanding I can have them afterwards!

My logo can be retrieved via this Dropbox link...
You'll notice there are 2 styles of placement. Please feel free to use either to fit in with your design...
https://www.filebarrow.net/sh/kq7pw2mzt4xn8bc/BBBLqr5hoPnvtc6S41MkwvaHb?dl=0

The wedding images I have are in this Dropbox folder...
https://www.filebarrow.net/sh/r8ym3vk6fa2lp9q/BBB4dzrTy8kW5nh63LxPeqjsc?dl=0

Other than that, it's over to you.... I can't wait to receive your designs :-)

Ooh....finally just to say, as I receive designs in I think I'll notice aspects that I like and don't like and if I feel they'll be useful for other designers, I'll update my brief below. Thanks

BRIEF UPDATE:
Someone asked if I had a tag-line. Could you use "Creating exquisite occasions today for amazing memories tomorrow"

I realise I hadn't explained what I'd like included on my home page so here's some notes to consider....

A welcome to section for me to start narrative about us and our services which has a button that links to our 'about us' page and 'services' page for further information.

A section that nicely illustrates what services we offer whether that be with icons or pictures.

A section with some photos in that would link to our gallery

A section that shows some customer reviews and blog entries that would link to my reviews page and blog to read more.

And finally a contact us section with my details, social media links and site map.

***
I also need to draw attention to where in the UK my services cover. I was therefore thinking perhaps we could use a picture to demonstrate this where it highlights Wiltshire, Oxfordshire, Berkshire and London on a map thereby demonstrating our areas covered. I have found several English county maps when searching on Google but I'm not sure how to highlight the areas I cover (or dull out the areas I don't) so if you have any ideas on this, I'd really like it incorporated. Thanks. (by the way, for those of you not familiar with English counties, the ones I cover are often abbreviated to Wilts, Oxon, Berks, London, so if you find a suitable map with those names on rather than the full names, you'll know what they are!)

I've found an image of the county map which might work well. I was wondering whether we might somehow grey out the counties I don't cover and just keep the ones I do as mentioned above and then crop it into perhaps a shadowed circle? I've attached a screenshot to the brief.
Updates

I've decided on the tag-line "Creating exquisite occasions today for amazing memories tomorrow" so if that could be included somewhere that would be great. I also need to draw attention to where in the UK my services cover. I was therefore thinking perhaps we could use a picture to demonstrate this where it highlights Wiltshire, Oxfordshire, Berkshire and London on a map thereby demonstrating our areas covered. I have found several English county maps when searching on Google but I'm not sure how to highlight the areas I cover (or dull out the areas I don't) so if you have any ideas on this, I'd really like it incorporated. Thanks. Added Wednesday, June 24, 2015

Target Market(s)

Predominately women aged 25-55

Industry/Entity Type

Wedding Planner

Number of Pages Required

1 page

Font styles to use
Sans Serif
Script

Requirements
Nice to have
• I'd like to see how the colour theme of purple and perhaps a little gold (maybe as a font colour) look against a white background. I've mentioned the Pantone colours in the brief above.
• I've attached a screenshot of a webpage with gold writing in and fonts that I like. Perhaps it could give you inspiration?
Should not have
• I really don't like the font SCRIPTINA so please done use that.

```html
<!DOCTYPE html>
<html lang="en">
<head>
<meta charset="utf-8">
<title>Silver Fern Gatherings</title>
<link rel="stylesheet" href="https://fonts.googleapis.com/css2?family=Great+Vibes&family=Open+Sans:wght@400;600;700&display=swap">
<style>
:root{
  --purple:#8f2a91;
  --purple-soft:#a54aa6;
  --gold:#d39a3c;
  --ink:#555555;
  --ink-soft:#777777;
  --page:#ffffff;
  --band:#f7f7f7;
  --footer:#f2f2f2;
  --rule:#cfcfcf;
  --frame:#e4d9cd;
}
*{box-sizing:border-box;margin:0;padding:0}
html,body{width:1200px;height:2333px;overflow:hidden}
body{position:relative;background:var(--page);font-family:"Open Sans",Arial,sans-serif;color:var(--ink)}
.abs{position:absolute}
.script{font-family:"Great Vibes",cursive;font-weight:400}

/* header */
.site-header{position:absolute;left:0;top:0;width:1200px;height:86px;background:linear-gradient(#fff 60%,#f3eef4)}
.brand{position:absolute;left:193px;top:26px;display:flex;align-items:center;gap:10px;color:var(--purple);font-size:22px;font-weight:600;letter-spacing:.3px}
.brand-dot{width:28px;height:28px;border-radius:50%;background:var(--purple)}
.main-nav{position:absolute;left:506px;top:30px;display:flex;font-size:17px;color:#666}
.main-nav a{color:inherit;text-decoration:none}
.main-nav .sep{margin:0 21px;color:#bbb}
.main-nav .active{color:var(--purple);font-weight:600}

/* hero */
.hero{position:absolute;left:0;top:86px;width:1200px;height:465px;background:linear-gradient(100deg,#6f8d3a 0%,#9cb45a 35%,#c9cfa8 55%,#e8e2d8 70%,#3b3f44 85%,#6a7a3a 100%)}
.hero-caption{position:absolute;left:72px;top:124px;width:491px;height:230px;background:rgba(40,40,40,.72);color:#fff;text-align:center}
.hero-caption h1{font-size:40px;line-height:40px;margin-top:24px}
.hero-caption p{font-size:11.5px;line-height:16px;margin:14px 44px 0}
.btn{display:inline-block;border:2px solid var(--gold);color:var(--gold);font-size:13px;font-weight:700;letter-spacing:.5px;text-transform:uppercase;text-decoration:none;height:36px;line-height:32px;padding:0 14px;border-radius:2px;background:#fff}
.hero-caption .btn{background:transparent;margin-top:20px;padding:0 10px}
.hero-arrow{position:absolute;top:222px;width:24px;height:30px}
.hero-tab{position:absolute;left:366px;top:420px;width:459px;height:45px}
.dots{position:absolute;display:flex;gap:13px}
.dots span{width:16px;height:16px;border-radius:50%;background:#e6d6b8}
.dots span.on{background:var(--purple)}

/* sections */
.band{position:absolute;left:0;width:1200px}
.welcome{top:551px;height:246px;background:var(--band);text-align:center}
.welcome h2{font-size:48px;color:var(--ink);margin-top:27px;line-height:56px}
.welcome h2 em{font-style:normal;color:var(--gold)}
.welcome p{width:692px;margin:14px auto 0;font-size:13.5px;line-height:21.5px;color:#666}
.welcome .btn{margin-top:28px}

.section-title{font-size:44px;color:var(--gold);text-align:center;line-height:50px}
.rule{position:absolute;left:522px;width:156px;height:8px}

.services{top:797px;height:471px;background:var(--page)}
.services .section-title{margin-top:30px}
.services .lead{position:absolute;left:330px;top:108px;width:540px;text-align:center;font-size:10.5px;font-style:italic;line-height:13px;color:#555}
.service{position:absolute;top:156px;width:200px;text-align:center}
.service .photo{width:150px;height:150px;margin:0 auto;border-radius:50%;border:7px solid var(--frame)}
.service h3{font-size:26px;color:var(--purple);margin-top:14px;line-height:30px}
.service p{font-size:10.5px;line-height:14px;color:#666;margin-top:2px;padding:0 26px}
.services .btn{position:absolute;left:548px;top:414px}

.gallery{top:1268px;height:374px;background:var(--band)}
.gallery .section-title{margin-top:20px}
.gallery-strip{position:absolute;left:0;top:115px;display:flex;gap:3px}
.gallery-strip div{width:131px;height:128px}
.gallery .btn{position:absolute;left:548px;top:322px}

.blog{top:1642px;height:475px;background:var(--page)}
.blog .section-title{margin-top:26px}
.post{position:absolute;top:108px;width:196px;height:267px;background:#f7f7f7;border-top:3px solid #e9cf9c;padding:5px}
.post .photo{position:relative;height:125px}
.date{position:absolute;left:0;top:36px;width:44px;height:51px;background:var(--purple-soft);color:#fff;text-align:center}
.date b{display:block;font-size:22px;line-height:28px;font-weight:600}
.date small{display:block;font-size:7px;line-height:10px}
.post h4{font-family:"Great Vibes",cursive;font-weight:400;font-size:15px;line-height:14px;color:#333;margin:12px 3px 0}
.post .meta{font-size:8px;color:var(--gold);margin:5px 3px 0;font-style:italic}
.post .meta span{color:#aaa;margin:0 3px}
.post .excerpt{font-size:8.5px;line-height:11px;color:#666;margin:2px 3px 0}
.read-more{position:absolute;right:8px;bottom:12px;font-size:8.5px;color:var(--purple);display:flex;align-items:center;gap:4px}
.read-more i{width:8px;height:8px;border-radius:50%;background:var(--purple)}
.blog .btn{position:absolute;left:548px;top:398px}

/* footer */
.site-footer{position:absolute;left:0;top:2117px;width:1200px;height:216px;background:var(--footer);border-top:2px solid #e9cf9c}
.footer-col{position:absolute;top:24px}
.footer-col h5{font-size:12.5px;font-weight:700;color:#444;letter-spacing:.3px}
.footer-brand{display:flex;align-items:center;gap:7px;color:var(--purple);font-size:15px;font-weight:600;margin-top:22px}
.footer-brand i{width:18px;height:18px;border-radius:50%;background:var(--purple)}
.footer-col p{font-size:10px;line-height:14px;color:#555}
.footer-col ul{list-style:none;margin-top:18px}
.footer-col li{font-size:10.5px;line-height:22px;color:#444}
.info-row{display:flex;gap:10px;font-size:10.5px;line-height:14px;color:#444}
.info-row svg{flex:none;margin-top:1px}
.social{display:flex;gap:9px;margin-top:24px}
.social span{width:20px;height:20px;background:#b9b9b9;border-radius:3px}
.copyright{font-size:9px;line-height:13px;color:#444;text-align:center;margin-top:28px}
</style>
</head>
<body>

<header class="site-header">
  <div class="brand"><span class="brand-dot"></span>Silver Fern Gatherings</div>
  <nav class="main-nav">
    <a class="active" href="#">Home</a><span class="sep">/</span>
    <a href="#">About</a><span class="sep">/</span>
    <a href="#">Services</a><span class="sep">/</span>
    <a href="#">Gallery</a><span class="sep">/</span>
    <a href="#">Blog</a><span class="sep">/</span>
    <a href="#">Contact</a>
  </nav>
</header>

<section class="hero" role="img" aria-label="Bride in a veil and groom in a dark suit smiling outdoors against a green garden">
  <div class="hero-caption">
    <h1 class="script">Creating exquisite occasions today<br>for amazing memories tomorrow</h1>
    <p>Etiamursus leo vel metus. Nulla facilisi. Aec eros. Vestibulum ante ipsu primis in faucibus orci luctus et trices posuere cubilia Suspendisse sollici. Scelerisque</p>
    <a class="btn" href="#">Learn More</a>
  </div>
  <svg class="hero-arrow" style="left:24px" viewBox="0 0 24 30"><path d="M17 4 7 15l10 11" fill="none" stroke="#fff" stroke-width="4"/></svg>
  <svg class="hero-arrow" style="left:1150px" viewBox="0 0 24 30"><path d="M7 4l10 11L7 26" fill="none" stroke="#fff" stroke-width="4"/></svg>
  <svg class="hero-tab" viewBox="0 0 459 45"><path d="M12 0H447L459 45H0Z" fill="#f7f7f7"/></svg>
  <div class="dots" style="left:563px;top:437px"><span></span><span class="on"></span><span></span></div>
</section>

<section class="band welcome">
  <h2 class="script">Welcome to <em>Silver Fern</em></h2>
  <p>Lorem ipsum dolor sit amet, consectetur adipisicing elit, sed do eiusmod tempor incididunt ut labore et dolore magna aliqua. Ut enim ad minim veniam, quis nostrud exercitation ullamco laboris nisi ut aliquip commodo consequat. Duis aute irure dolor in reprehenderit in voluptate velit esse cillum dolore eu cupidatat non prdeser</p>
  <a class="btn" href="#">A bout us</a>
</section>

<section class="band services">
  <h2 class="section-title script">Our services</h2>
  <svg class="rule" style="top:82px" viewBox="0 0 156 8"><line x1="0" y1="4" x2="66" y2="4" stroke="var(--rule)" stroke-width="2"/><rect x="74" y="0" width="8" height="8" transform="rotate(45 78 4)" fill="var(--rule)"/><line x1="90" y1="4" x2="156" y2="4" stroke="var(--rule)" stroke-width="2"/></svg>
  <p class="lead">Lorem ipsum dolor sit amet, consectetur adipisicing elit, sed do eiusmod tempor incididunt ut labore et dolore magna aliqua. Ut enim ad minim veniam, quis nostrud exercitation ullamco</p>
  <div class="service" style="left:166px">
    <div class="photo" role="img" aria-label="Two hands exchanging wedding rings" style="background:radial-gradient(circle at 45% 45%,#e8b69a,#9cc24a 60%,#6f9a2a)"></div>
    <h3 class="script">Wedding Planning</h3>
    <p>Lorem ipsum dolor sit amet, consectetur adipisicing elit. Non, dignissimos nihil unde.</p>
  </div>
  <div class="service" style="left:387px">
    <div class="photo" role="img" aria-label="Children celebrating at a birthday party" style="background:radial-gradient(circle at 50% 55%,#e3b04a,#5f9ad0 55%,#3f7a3a)"></div>
    <h3 class="script">Birthdays</h3>
    <p>Lorem ipsum dolor sit amet, consectetur adipisicing elit. Non, dignissimos nihil unde.</p>
  </div>
  <div class="service" style="left:608px">
    <div class="photo" role="img" aria-label="Model in red shoes walking a fashion runway" style="background:radial-gradient(circle at 50% 50%,#e2502a,#a8210f 60%,#5a0f08)"></div>
    <h3 class="script">Fashion shows</h3>
    <p>Lorem ipsum dolor sit amet, consectetur adipisicing elit. Non, dignissimos nihil unde.</p>
  </div>
  <div class="service" style="left:829px">
    <div class="photo" role="img" aria-label="Audience watching a conference presentation" style="background:radial-gradient(circle at 50% 30%,#f2f2f2,#b9b3ad 50%,#4a4644)"></div>
    <h3 class="script">Conferences</h3>
    <p>Lorem ipsum dolor sit amet, consectetur adipisicing elit. Non, dignissimos nihil unde.</p>
  </div>
  <a class="btn" href="#">Know more</a>
</section>

<section class="band gallery">
  <h2 class="section-title script">Gallery</h2>
  <svg class="rule" style="top:70px" viewBox="0 0 156 8"><line x1="0" y1="4" x2="66" y2="4" stroke="var(--rule)" stroke-width="2"/><rect x="74" y="0" width="8" height="8" transform="rotate(45 78 4)" fill="var(--rule)"/><line x1="90" y1="4" x2="156" y2="4" stroke="var(--rule)" stroke-width="2"/></svg>
  <div class="gallery-strip">
    <div role="img" aria-label="Couple's hands holding rings" style="background:linear-gradient(135deg,#c9d3dc,#d9a98f)"></div>
    <div role="img" aria-label="Bride holding a white bouquet" style="background:linear-gradient(135deg,#8a5a3a,#ece6dc)"></div>
    <div role="img" aria-label="Back of a lace-up wedding dress" style="background:linear-gradient(135deg,#d7b08c,#f2ece4)"></div>
    <div role="img" aria-label="Glasses on a set reception table" style="background:linear-gradient(135deg,#7a4a24,#d8d2ca)"></div>
    <div role="img" aria-label="Reception table with plates and flowers" style="background:linear-gradient(135deg,#9fb07a,#e6e2da)"></div>
    <div role="img" aria-label="Roses with gold wedding rings" style="background:linear-gradient(135deg,#f4eeea,#e6b8b2)"></div>
    <div role="img" aria-label="Flower girl in a white dress outdoors" style="background:linear-gradient(135deg,#6f8a4a,#efe9e4)"></div>
    <div role="img" aria-label="Waiter serving plated dishes" style="background:linear-gradient(135deg,#e2ddd6,#b58f70)"></div>
    <div role="img" aria-label="Purple lit banquet hall with floral centrepieces" style="background:linear-gradient(135deg,#6b4a9a,#c9a9d8)"></div>
  </div>
  <div class="dots" style="left:563px;top:277px"><span></span><span class="on"></span><span></span></div>
  <a class="btn" href="#">Gallerie</a>
</section>

<section class="band blog">
  <h2 class="section-title script">Our blog</h2>
  <svg class="rule" style="top:80px" viewBox="0 0 156 8"><line x1="0" y1="4" x2="66" y2="4" stroke="var(--rule)" stroke-width="2"/><rect x="74" y="0" width="8" height="8" transform="rotate(45 78 4)" fill="var(--rule)"/><line x1="90" y1="4" x2="156" y2="4" stroke="var(--rule)" stroke-width="2"/></svg>

  <article class="post" style="left:185px">
    <div class="photo" role="img" aria-label="Waiter serving plated dishes at a reception" style="background:linear-gradient(135deg,#d9d4cc,#a97f60)"><div class="date"><b>09</b><small>JUN, 2015</small></div></div>
    <h4>Lorem ipsum dolor sit amet, title consectetur</h4>
    <p class="meta">By Admin<span>/</span>0 Comment<span>/</span>Wedding</p>
    <p class="excerpt">Lorem ipsum dolor sit amet, consectetur adipisicing elit. Non ut labore et dolore magna et sed aliqua et enim.</p>
    <span class="read-more"><i></i>Read More</span>
  </article>
  <article class="post" style="left:397px">
    <div class="photo" role="img" aria-label="Pale roses beside gold wedding rings" style="background:linear-gradient(135deg,#f4eee8,#e4bfb5)"><div class="date"><b>11</b><small>MAR, 2015</small></div></div>
    <h4>Lorem ipsum dolor sit amet, title consectetur</h4>
    <p class="meta">By Admin<span>/</span>0 Comment<span>/</span>Event</p>
    <p class="excerpt">Lorem ipsum dolor sit amet, consectetur adipisicing tempor et enim.</p>
    <span class="read-more"><i></i>Read More</span>
  </article>
  <article class="post" style="left:608px">
    <div class="photo" role="img" aria-label="Close view of coral pink roses" style="background:linear-gradient(135deg,#f08a70,#d9543c)"><div class="date"><b>12</b><small>JAN, 2015</small></div></div>
    <h4>Lorem ipsum dolor sit amet, title consectetur</h4>
    <p class="meta">By Admin<span>/</span>2 Comment<span>/</span>Blog</p>
    <p class="excerpt">Lorem ipsum dolor sit amet, consectetur adipisicing tempor incididun</p>
    <span class="read-more"><i></i>Read More</span>
  </article>
  <article class="post" style="left:820px">
    <div class="photo" role="img" aria-label="Bride holding a bouquet beside a table" style="background:linear-gradient(135deg,#e8e4dc,#8fa06a)"><div class="date"><b>01</b><small>JAN, 2015</small></div></div>
    <h4>Lorem ipsum dolor sit amet, title consectetur</h4>
    <p class="meta">By Admin<span>/</span>0 Comment<span>/</span>Blog</p>
    <p class="excerpt">dolor sit amet, consectetur adipisicing tempor incididunt ut labore et dolore magna et sed</p>
    <span class="read-more"><i></i>Read More</span>
  </article>
  <a class="btn" href="#">Go to blog</a>
</section>

<footer class="site-footer">
  <div class="footer-col" style="left:195px;width:180px">
    <h5>ABOUT US</h5>
    <div class="footer-brand"><i></i>Silver Fern Gatherings</div>
    <p style="margin-top:14px">Lorem ipsum dolor sit amet, consectetur adipisicing elit. Quam culpa, hic autem itaque. Natus, ducimus quis. Iusto quaerat harum atque earum illum reprehenderit nisi quasi odit, optio iure officiis eaque.</p>
  </div>
  <div class="footer-col" style="left:400px">
    <h5>CATEGORIES</h5>
    <ul><li>Home</li><li>About us</li><li>Our services</li><li>Gallery</li><li>Our blog</li><li>Contact</li></ul>
  </div>
  <div class="footer-col" style="left:610px;width:200px">
    <h5>INFO</h5>
    <div class="info-row" style="margin-top:20px"><svg width="12" height="12" viewBox="0 0 12 12"><circle cx="6" cy="6" r="5" fill="none" stroke="var(--purple)" stroke-width="1.6"/><path d="M6 3v3h2" stroke="var(--purple)" stroke-width="1.4" fill="none"/></svg>Monday – Friday (9:00am – 5:00pm)</div>
    <div class="info-row" style="margin-top:14px"><svg width="12" height="14" viewBox="0 0 12 14"><path d="M6 13S1 8 1 5a5 5 0 0 1 10 0c0 3-5 8-5 8z" fill="var(--purple)"/><circle cx="6" cy="5" r="1.8" fill="#fff"/></svg>PO 1232 Your Road, M09 77 R<br>City - country</div>
    <div class="info-row" style="margin-top:16px"><svg width="12" height="12" viewBox="0 0 12 12"><path d="M1 6 11 1 8 11 6 7z" fill="var(--purple)"/></svg>maureen@silverferngatherings.co.uk</div>
    <div class="info-row" style="margin-top:14px;font-weight:600"><svg width="12" height="12" viewBox="0 0 12 12"><path d="M2 1h3l1 3-2 1c1 2 2 3 3 3l1-2 3 1v3c-6 1-10-3-9-9z" fill="var(--purple)"/></svg>01632 960571 &nbsp;/&nbsp; 07700 900384</div>
  </div>
  <div class="footer-col" style="left:830px;width:170px">
    <h5>SOCIAL</h5>
    <div class="social" style="margin-left:26px"><span></span><span></span><span></span><span></span><span></span></div>
    <p class="copyright">Copyright ©2015 Silver Fern Gatherings.<br>All rights reserved</p>
  </div>
</footer>

</body>
</html>
```